The name of the company is Kestrel Rehab buying foreclosed homes and remodeling

A sleek classy card. It’s a home remodel and house flip company. Something mostly black with dark gray and red in color . Something with two f”s as a logo on front as shown in pictures. Kind of just let you guys run with it . I left a few pictures that should help
You guys get an idea of what I thought was good also left all the information for back of the card

Target Market(s)

Home remodel consumers

Industry/Entity Type

Construction Company

Contact Information for Business Card

All details are on photo

Font styles to use
Decorative

Colors

Designer to choose colors to be used in the design.

Requirements
Must have
• Name of company on front. Kestrel Rehab
Nice to have
• Up to you guys I trust you
Should not have
• Not sure

```html
<!DOCTYPE html>
<html lang="en">
<head>
<meta charset="utf-8">
<title>Kestrel Rehab – Business Card</title>
<link rel="stylesheet" href="https://fonts.googleapis.com/css2?family=Libre+Baskerville:ital@1&family=Open+Sans:wdth,wght@75..100,400..700&display=swap">
<style>
  :root {
    --page: #ffffff;
    --card-front: #000000;
    --card-back: #c0c1c3;
    --card-edge: #8f9092;
    --mark-gray: #4a4a4a;
    --mark-faint: #cfd0d2;
    --accent-red: #b3364f;
    --ink: #111111;
  }
  * { margin: 0; padding: 0; box-sizing: border-box; }
  html, body {
    width: 927px; height: 1200px; overflow: hidden;
    background: var(--page);
  }
  .sheet { position: relative; width: 927px; height: 1200px; }

  .card { position: absolute; width: 382px; height: 218px; overflow: hidden; }

  /* Front */
  .card--front { left: 289px; top: 308px; background: var(--card-front); }
  .front-mark {
    position: absolute; left: 18px; top: 150px;
    width: 34px; height: 34px; border-radius: 50%;
    background: var(--mark-gray);
  }
  .front-name {
    position: absolute; left: 85px; top: 154px;
    font-family: "Open Sans", sans-serif;
    font-stretch: 75%; font-weight: 400;
    font-size: 19px; color: var(--accent-red);
    letter-spacing: 0.2px;
  }

  /* Back */
  .card--back {
    left: 285px; top: 612px;
    background: var(--card-back);
    border: 1px solid var(--card-edge);
  }
  .back-mark {
    position: absolute; left: 14px; top: 10px;
    width: 96px; height: 96px;
    background: var(--mark-faint); opacity: 0.55;
  }
  .holder {
    position: absolute; right: 17px; top: 11px;
    font-family: "Open Sans", sans-serif;
    font-stretch: 75%; font-weight: 700;
    font-size: 13.5px; color: var(--accent-red);
  }
  .holder-rule {
    position: absolute; left: 203px; top: 34px;
    width: 35px; height: 1.5px; background: var(--accent-red);
  }
  .contact-list {
    position: absolute; left: 44px; top: 64px;
    list-style: none;
  }
  .contact-item {
    display: flex; align-items: baseline;
    height: 20.5px;
  }
  .contact-label {
    width: 32px; text-align: right; padding-right: 8px;
    font-family: "Libre Baskerville", serif; font-style: italic;
    font-size: 12px; color: var(--accent-red);
  }
  .contact-value {
    font-family: "Open Sans", sans-serif;
    font-stretch: 75%; font-size: 14px; color: var(--ink);
  }
  .services {
    position: absolute; left: 76px; top: 174px;
    font-family: "Open Sans", sans-serif;
    font-stretch: 75%; font-size: 11.5px; color: var(--ink);
    word-spacing: 1px;
  }
  .services span + span { margin-left: 7px; }
</style>
</head>
<body>
<main class="sheet">
  <section class="card card--front" aria-label="Card front">
    <div class="front-mark"></div>
    <p class="front-name">Kestrel Rehab</p>
  </section>

  <section class="card card--back" aria-label="Card back">
    <div class="back-mark"></div>
    <p class="holder">Marcus Albright, Jr.</p>
    <div class="holder-rule"></div>
    <ul class="contact-list">
      <li class="contact-item"><span class="contact-label">t:</span><span class="contact-value">555&nbsp; 014&nbsp; 2287</span></li>
      <li class="contact-item"><span class="contact-label">e:</span><span class="contact-value">malbrightjr@example.com</span></li>
      <li class="contact-item"><span class="contact-label">w:</span><span class="contact-value">www. kestrelrehab.com</span></li>
      <li class="contact-item"><span class="contact-label">i:</span><span class="contact-value">Kestrel_Rehab</span></li>
    </ul>
    <p class="services"><span>General Contractor</span><span>Home Remodel</span><span>Concrete Alternatives</span></p>
  </section>
</main>
</body>
</html>
```